Saveurs Du Matin

looking fo an e-commerce site something that will stand out the site domain will be saveursdumatin.example need somthing bold and refind as well; eye appealing and not too cartonish please visit our competetors to see waht we are going for they are (zestlyne.example, brantaro4u.example and quellabrookfarms.example) this site should have multiple pages mainly looking for a layout to start the site and code.

PLEASE REMEMBER WE REQUIRE THE CODE....

Target Market(s)

anyone who loves food or is fasinated by it

Industry/Entity Type

E-Commerce

Requirements
Must have
• .an easy to work site that makes sense and that is not all over the place it should have in the navigation feature: Olive oils, Balsamic Vinegars, Misc. Vinegars and oils, Specialty salts, organic spices, Specialty Spices, Kitchen Tools. also pleas use our logo in the design i have attached below
Nice to have
• clean and some spices, salt, pepermills, morter and pistels, olive oils, trying to stick to a clean presentation
Should not have
• no cartoon figures or alike, anything too playfull

```html
<!DOCTYPE html>
<html lang="en">
<head>
<meta charset="utf-8">
<title>Saveurs Du Matin</title>
<link rel="stylesheet" href="https://fonts.googleapis.com/css2?family=Kreon:wght@400;500&family=Open+Sans:ital,wght@0,400;0,600;1,400&display=swap">
<style>
:root{
  --accent:#b0602c;
  --accent-dark:#8e4519;
  --peach:#edc6a2;
  --peach-light:#f3d6bb;
  --peach-deep:#e2b189;
  --ink:#333;
  --muted:#666;
  --line:#e2e2e2;
  --paper:#fff;
  --tag:#d98c5f;
  --tag-dark:#b8643a;
}
*{box-sizing:border-box;margin:0;padding:0}
html,body{width:920px;height:1200px;overflow:hidden;background:var(--paper)}
body{position:relative;font-family:"Open Sans",Arial,sans-serif;color:var(--ink);font-size:11px}
.abs{position:absolute}
.stripe{left:0;width:920px;height:5px;background:linear-gradient(90deg,#9c4a1c,#c8762f 20%,#8a3a15 40%,#d39a3c 60%,#9c4a1c 80%,#c8762f)}
.brand{display:flex;align-items:center;gap:10px}
.brand-mark{width:40px;height:40px;border-radius:50%;border:2px solid var(--accent)}
.brand-name{font-family:"Kreon",Georgia,serif;font-size:28px;color:var(--accent);font-weight:400;white-space:nowrap}
.account{top:44px;left:604px;font-size:9px;display:flex;gap:12px;color:#222}
.search{top:39px;left:733px;width:96px;height:22px;border:1px solid #ddd;font-size:9px;font-style:italic;color:#aaa;padding:5px 8px}
.search svg{position:absolute;right:6px;top:5px}
.nav{top:78px;left:92px;width:736px;height:40px;border-top:1px solid var(--line);display:flex;justify-content:space-between;font-size:11px;white-space:nowrap}
.nav a{color:#333;text-decoration:none;line-height:40px;padding:0 8px}
.nav .active{color:var(--accent);border-left:1px solid var(--line);border-right:1px solid var(--line);background:linear-gradient(#f6f6f6,#fff)}
.hero{top:118px;left:0;width:920px;height:262px;background:var(--peach);border-top:1px dashed #fff;border-bottom:1px dashed #fff;box-shadow:inset 0 1px 0 var(--peach-deep)}
.hero-photo{left:152px;top:34px;width:260px;height:170px;border:3px solid var(--peach-light);background:linear-gradient(135deg,#7a3a1a,#c08a3a 40%,#5a2a12 70%,#a8602a);box-shadow:0 2px 6px rgba(0,0,0,.3)}
.ribbon{top:186px;height:20px;background:var(--accent-dark);color:#fbe3c8;font-size:8px;line-height:20px;text-align:center;text-transform:uppercase}
.price-flag{left:258px;top:168px;width:48px;height:58px;background:var(--accent);color:#fff;text-align:center;clip-path:polygon(0 0,100% 0,100% 100%,50% 85%,0 100%)}
.price-flag b{display:block;font-family:"Kreon",serif;font-weight:400;font-size:15px;margin-top:22px}
.arrow{top:122px;width:20px;height:34px;background:#fff;box-shadow:0 1px 3px rgba(0,0,0,.3);display:flex;align-items:center;justify-content:center}
.hero h1{left:488px;top:86px;font-family:"Kreon",serif;font-weight:400;font-size:27px;color:var(--accent-dark)}
.hero p{left:488px;top:122px;width:280px;color:#fff;font-size:10.5px;line-height:16px}
.btn-pill{left:692px;top:196px;width:64px;height:20px;border-radius:10px;background:#fff;font-size:9px;line-height:20px;text-align:center;color:#333}
.dots{left:440px;top:238px;display:flex;gap:3px}
.dots i{width:6px;height:6px;border-radius:50%;background:#f4e2d0}
.dots i:first-child{background:#fff}
.tab{height:28px;border:1px solid #ddd;background:linear-gradient(#fff,#f1f1f1);font-size:11px;line-height:26px;text-align:center;text-transform:uppercase}
.photo{background:radial-gradient(circle at 50% 55%,#6f7a3a,#b8a36a 55%,#fff 75%)}
.photo.mortar{background:radial-gradient(circle at 50% 60%,#b0892e,#d9bd6a 45%,#fff 72%)}
.photo.jars{background:radial-gradient(circle at 50% 55%,#2c3b35,#c4512e 45%,#fff 72%)}
.tag{width:40px;height:42px;background:var(--tag);border:1px dashed #f6d3bc;outline:1px solid var(--tag-dark);color:#fff;font-family:"Kreon",serif;font-size:13px;text-align:center;line-height:42px}
.tag::before{content:"$";position:absolute;top:-11px;left:13px;width:13px;height:13px;border-radius:50%;background:var(--tag-dark);font-size:8px;line-height:13px;font-family:"Open Sans",sans-serif}
.pname{font-family:"Kreon",serif;font-size:13px;color:#333;text-align:center;width:140px}
.btns{display:flex;border:1px solid #ccc;height:17px;font-size:7px;text-transform:uppercase;color:#666;background:linear-gradient(#fff,#eee)}
.btns span{padding:0 7px;line-height:15px;border-right:1px solid #ccc}
.btns span:last-child{border:0}
.sidebar{left:620px;top:608px;width:208px;height:466px;background:linear-gradient(90deg,#ebebeb,#fff 30%)}
.sidebar h3{font-family:"Kreon",serif;font-weight:400;font-size:13px;margin:16px 0 0 16px}
.sidebar ul{list-style:none;margin:24px 0 0 30px;font-size:9.5px;line-height:19.2px;color:#444;white-space:nowrap}
.sidebar li::before{content:"›";margin-right:5px;color:#444}
.sidebar hr{border:0;border-top:1px solid #e6e6e6;margin:18px 0 0 0}
.pop{left:118px;top:684px;width:262px;height:196px;background:#fff;border:1px solid #ddd;border-radius:4px;box-shadow:0 2px 8px rgba(0,0,0,.2);padding:20px 22px}
.pop h4{font-family:"Kreon",serif;font-weight:400;font-size:14px}
.pop .cost{position:absolute;right:22px;top:14px;font-family:"Kreon",serif;font-size:19px;color:var(--accent)}
.rate{display:flex;gap:6px;margin:14px 0 14px -4px}
.rate span{border:1px solid #ddd;border-radius:3px;padding:2px 6px;font-size:9px;font-style:italic}
.rate b{color:#f0b400;font-weight:400;letter-spacing:-1px}
.rate em{color:#ccc;font-style:normal}
.pop p{font-size:9px;line-height:18px;color:#444}
.pager{top:972px;left:400px;display:flex;align-items:center;gap:18px;font-size:11px}
.pager em{font-size:9px}
.pager .on{border:1px solid #ddd;background:#f4f4f4;width:32px;height:28px;text-align:center;line-height:26px}
.foot{top:1074px;left:0;width:920px;height:68px;background:var(--peach);border-top:1px dashed #fff;border-bottom:1px dashed #fff;box-shadow:inset 0 1px 0 var(--peach-deep)}
.sub{left:340px;top:24px;font-family:"Kreon",serif;font-size:13px;color:var(--accent-dark)}
.email{left:562px;top:16px;width:228px;height:32px;background:#fff;border-radius:4px;font-size:9px;color:#555;line-height:32px;padding-left:16px}
.go{left:788px;top:16px;width:38px;height:32px;background:var(--accent);border-radius:0 4px 4px 0;color:#fff;font-size:13px;line-height:32px;text-align:center}
.bnav{top:1163px;left:92px;display:flex;gap:7px;font-size:9px;white-space:nowrap}
.bnav .active{color:var(--accent)}
.copy{top:1163px;left:628px;font-size:8.5px;width:200px;text-align:right;white-space:nowrap}
</style>
</head>
<body>
<div class="abs stripe" style="top:0"></div>

<header>
  <div class="abs brand" style="left:92px;top:22px"><span class="brand-mark"></span><span class="brand-name">Saveurs Du Matin</span></div>
  <div class="abs account"><span>My Account</span><span>Login/Register</span></div>
  <div class="abs search">Search...<svg width="10" height="10" viewBox="0 0 10 10"><circle cx="6" cy="4" r="3" fill="none" stroke="#aaa"/><path d="M4 6L1 9" stroke="#aaa"/></svg></div>
  <nav class="abs nav">
    <a class="active">Olive Oils</a><a>Balsamic Vinegars</a><a>Misc. Vinegars &amp; Oils</a><a>Specialty Salts</a><a>Organic Spices</a><a>Specialty Spices</a><a>Kitchen Tools</a>
  </nav>
</header>

<section class="abs hero">
  <div class="abs hero-photo" role="img" aria-label="Wooden tray of assorted spices in square compartments"></div>
  <div class="abs ribbon" style="left:178px;width:82px">Add to cart</div>
  <div class="abs ribbon" style="left:304px;width:82px">More info</div>
  <div class="abs price-flag"><b>239</b></div>
  <div class="abs arrow" style="left:92px"><svg width="8" height="10"><path d="M6 1L2 5l4 4" fill="none" stroke="#444" stroke-width="2"/></svg></div>
  <div class="abs arrow" style="left:808px"><svg width="8" height="10"><path d="M2 1l4 4-4 4" fill="none" stroke="#444" stroke-width="2"/></svg></div>
  <h1 class="abs">Original Spices</h1>
  <p class="abs">Sed vel ante est, et molestie magna. Aenean non est id dolor tempus laoreet in non odio. Proin egestas erat et metus consequat vitae lacinia ligula auctor. Sed vehicula quam tincidunt lorem dignissim condimentum.</p>
  <div class="abs btn-pill">More Info</div>
  <div class="abs dots"><i></i><i></i><i></i><i></i></div>
</section>

<div class="abs tab" style="left:410px;top:371px;width:104px">Special Offers</div>

<section class="offers">
  <div class="abs photo" style="left:92px;top:400px;width:130px;height:112px" role="img" aria-label="Jar of green olives with cloth lid"></div><div class="abs tag" style="left:101px;top:423px">239</div><div class="abs pname" style="left:91px;top:516px">Calvena Olives</div><div class="abs btns" style="left:104px;top:538px"><span>Add to cart</span><span>More info</span></div>
  <div class="abs photo" style="left:246px;top:400px;width:130px;height:112px" role="img" aria-label="Jar of green olives with cloth lid"></div><div class="abs tag" style="left:255px;top:423px">239</div><div class="abs pname" style="left:245px;top:516px">Calvena Olives</div><div class="abs btns" style="left:254px;top:538px"><span>Add to cart</span><span>More info</span></div>
  <div class="abs photo" style="left:398px;top:400px;width:130px;height:112px" role="img" aria-label="Jar of green olives with cloth lid"></div><div class="abs tag" style="left:407px;top:423px">239</div><div class="abs pname" style="left:397px;top:516px">Calvena Olives</div><div class="abs btns" style="left:406px;top:538px"><span>Add to cart</span><span>More info</span></div>
  <div class="abs photo" style="left:550px;top:400px;width:130px;height:112px" role="img" aria-label="Jar of green olives with cloth lid"></div><div class="abs tag" style="left:559px;top:423px">239</div><div class="abs pname" style="left:549px;top:516px">Calvena Olives</div><div class="abs btns" style="left:558px;top:538px"><span>Add to cart</span><span>More info</span></div>
  <div class="abs photo" style="left:704px;top:400px;width:130px;height:112px" role="img" aria-label="Jar of green olives with cloth lid"></div><div class="abs tag" style="left:713px;top:423px">239</div><div class="abs pname" style="left:700px;top:516px">Calvena Olives</div><div class="abs btns" style="left:714px;top:538px"><span>Add to cart</span><span>More info</span></div>
</section>

<div class="abs" style="left:92px;top:607px;width:528px;border-top:1px solid var(--line)"></div>
<div class="abs tab" style="left:294px;top:594px;width:116px">Recent Products</div>

<section class="recent">
  <div class="abs photo mortar" style="left:100px;top:636px;width:90px;height:86px" role="img" aria-label="Brass mortar and pestle"></div><div class="abs tag" style="left:94px;top:650px">239</div>
  <div class="abs photo mortar" style="left:228px;top:636px;width:90px;height:86px" role="img" aria-label="Brass mortar and pestle"></div><div class="abs tag" style="left:223px;top:650px">239</div>
  <div class="abs photo mortar" style="left:356px;top:636px;width:90px;height:86px" role="img" aria-label="Brass mortar and pestle"></div><div class="abs tag" style="left:352px;top:650px">239</div>
  <div class="abs photo mortar" style="left:484px;top:636px;width:90px;height:86px" role="img" aria-label="Brass mortar and pestle"></div><div class="abs tag" style="left:480px;top:650px">239</div>
  <div class="abs pname" style="left:72px;top:731px">Morters and Pistels</div><div class="abs pname" style="left:329px;top:731px">Morters and Pistels</div><div class="abs pname" style="left:455px;top:731px">Morters and Pistels</div>
  <div class="abs btns" style="left:93px;top:752px"><span>Cart</span><span>? Info</span></div><div class="abs btns" style="left:223px;top:752px"><span>Cart</span><span>? Info</span></div><div class="abs btns" style="left:352px;top:752px"><span>Cart</span><span>? Info</span></div><div class="abs btns" style="left:481px;top:752px"><span>Cart</span><span>? Info</span></div>

  <div class="abs photo jars" style="left:100px;top:790px;width:90px;height:92px" role="img" aria-label="Glass spice jars with red and white herbs"></div><div class="abs tag" style="left:94px;top:806px">239</div>
  <div class="abs photo jars" style="left:228px;top:790px;width:90px;height:92px" role="img" aria-label="Glass spice jars with red and white herbs"></div><div class="abs tag" style="left:223px;top:806px">239</div>
  <div class="abs photo jars" style="left:356px;top:790px;width:90px;height:92px" role="img" aria-label="Glass spice jars with red and white herbs"></div><div class="abs tag" style="left:352px;top:806px">239</div>
  <div class="abs photo jars" style="left:484px;top:790px;width:90px;height:92px" role="img" aria-label="Glass spice jars with red and white herbs"></div><div class="abs tag" style="left:480px;top:806px">239</div>
  <div class="abs pname" style="left:65px;top:890px">Herbs Spices</div><div class="abs pname" style="left:197px;top:890px">Herbs Spices</div><div class="abs pname" style="left:326px;top:890px">Herbs Spices</div><div class="abs pname" style="left:453px;top:890px">Herbs Spices</div>
  <div class="abs btns" style="left:93px;top:912px"><span>Cart</span><span>? Info</span></div><div class="abs btns" style="left:223px;top:912px"><span>Cart</span><span>? Info</span></div><div class="abs btns" style="left:352px;top:912px"><span>Cart</span><span>? Info</span></div><div class="abs btns" style="left:481px;top:912px"><span>Cart</span><span>? Info</span></div>

  <div class="abs pop">
    <h4>Morters and Pistels</h4><span class="cost">$239</span>
    <div class="rate"><span>Author <b>★★</b><em>★★★</em></span><span>Users <b>★★★★★</b></span></div>
    <p>Duis ut velit id est accumsan volutpat ac id purus. Ut bibendum, mauris et pellentesque cursus, felis libero molestie urna, eget sagittis turpis felis ut justo. Nulla facilisi. Pellentesque habitant morbi tristique senectus et netus et malesuada fames ac</p>
  </div>

  <div class="abs pager"><em>Page 1 of 4</em><span class="on">1</span><span>2</span><span>3</span><span>4</span></div>
</section>

<aside class="abs sidebar">
  <h3>Popular Products</h3>
  <ul><li>Curabitur blandit rutrum nulla ac</li><li>Pharetra donec dictum felis eu</li><li>Eros pretium vulputate pretium vulpu</li><li>Etiam quis nulla ac turpis moles</li><li>Suspendisse potenti integer potenti</li><li>Accumsan nunc sollicitudin id</li><li>Pellentesque tortor lectus faucipotenti</li></ul>
  <hr>
  <h3>Recent Products</h3>
  <ul><li>Curabitur blandit rutrum nulla ac</li><li>Pharetra donec dictum felis eu</li><li>Eros pretium vulputate pretium vulpu</li><li>Etiam quis nulla ac turpis moles</li><li>Suspendisse potenti integer potenti</li><li>Accumsan nunc sollicitudin id</li><li>Pellentesque tortor lectus faucipotenti</li></ul>
  <hr>
</aside>

<footer>
  <div class="abs foot">
    <div class="abs brand" style="left:92px;top:14px"><span class="brand-mark" style="width:34px;height:34px"></span><span class="brand-name" style="font-size:21px">Saveurs Du Matin</span></div>
    <div class="abs sub">Subscribe to our newsletter now :</div>
    <div class="abs email">enter email address here</div>
    <div class="abs go">GO</div>
  </div>
  <nav class="abs bnav"><span class="active">Olive Oils</span><span>Balsamic Vinegars</span><span>Misc. Vinegars &amp; Oils</span><span>Specialty Salts</span><span>Organic Spices</span><span>Specialty Spices</span><span>Kitchen Tools</span></nav>
  <div class="abs copy">Copyright @ 2012. All Rights Reserved.</div>
</footer>

<div class="abs stripe" style="top:1193px;height:7px"></div>
</body>
</html>
```